Wine label design for a family winery in Slovenia

We need new label design for our wines.
We are small family wine producers who focuses on good quality wine and loves to experiment, mixing tradition with new, more modern approaches. Our main product is ‘Teran’, red wine whose character is highly defined by terroir: more acidic, but rich body and very rich, dark colour (we say it's not red, but black). We also age a small portion of this Teran wine with wood, which we named 'Pelmik' (after one of our vineyards). From the same grapes as Teran we also produce a small quantity of Rose. And we also produce two white wine varieties: one is 'Sopa', cuvee of several different sorts of grapes. The other is 'Ostrena', Chardonnay wine, named after another of our vineyards. Aside from all that we also produce liquour (Teranov liker) made from Teran wine and a small quantity of other spirits (Grappa, various fruit liquors, a version of Blaustrummer, and ‘Travarica’ which is grappa infused with various herbs and spices).
Sopa, Rose and Teran are considered our 'basic' line, whereas 'Pelmik' and 'Ostrena' are considered to be a higher quality line. Rose sits somewhere between this two.
In time we'd like to renew all of our labels. But the priority and subject of this ‘’project’’ is to create the two for our top line, Pelmik and Ostrena and also for Rose.
For 'Pelmik' we already have a template label. The general idea behind it was play with letters and divide them along the label (PE LM IK). We found that we like the narrow, longer dimensions and that black label on black bottle, with letters that stand out due to colour or printing differences, work very well. But we're amateurs and the label is not finalized. We would ask you to do something on this basis, but please don't limit yourself only to this if you have a better idea.
For 'Ostrena' the label should be in the same style to imply the same higher quality line - colours can and probably should be reversed to the lighter side (so to imply that it’s a white wine). Also, for this wine we'll use the same dark slender bottles, like you see on the image.
Please keep in mind that we'll print smaller series (1000-2000 pcs), so it must be possible to print the labels for a sensible cost. Solutions like classical offset gold print that requires large series of 10.000 pcs, will not work. But we can look into any digital printing/lacquering options that offer similar effects. Anyway, we are not experts on this field, so your advice on printing techniques is also welcomed.
Also, a word on our emblem: the logo is also not finalized and we will also ask you to work on it. The logo is part of the ornament on the doors of our homestead and represents a ‘kolovrat’ (‘spinning wheel’ in English), an old Slavic symbol for the sun, representing eternal life and spinning of time. We'd like to use it, but right now it's badly digitalized. If you'll need any better photos of it, let me know.

Target Market(s)

30-60 yo, red wine lovers, appreciate local and speicality wines

Font styles to use
Sans Serif
Decorative

Requirements
Must have
• long, narrow label dimensions (see attached Pelmik)

```html
<!DOCTYPE html>
<html lang="sl">
<head>
<meta charset="utf-8">
<title>Klet Dolinar – wine labels</title>
<link href="https://fonts.googleapis.com/css2?family=Cormorant+Garamond:wght@500&family=Lato:wght@300;400&display=swap" rel="stylesheet">
<style>
  :root{
    --bg:#ececec;
    --label-dark:#0b0b0b;
    --label-light:#ffffff;
    --red:#d3202a;
    --gold:#9a6a22;
    --rose:#dc8a9a;
    --text-dark:#9a9a9a;
    --text-light:#4a4a4a;
    --ink:#111111;
  }
  *{margin:0;padding:0;box-sizing:border-box}
  html,body{width:1200px;height:685px;overflow:hidden;background:var(--bg)}
  body{position:relative;font-family:"Lato",Arial,sans-serif}

  .label{position:absolute;overflow:hidden;text-align:center}
  .label--front{width:145px;height:247px;top:306px}
  .label--back{width:137px;height:184px;top:326px}
  .label--dark{background:var(--label-dark);color:var(--text-dark)}
  .label--light{background:var(--label-light);color:var(--text-light)}

  .year{position:absolute;top:10px;left:0;right:0;font-size:7px;letter-spacing:1px;font-weight:400}
  .label--dark .year{color:#e6e6e6}
  .label--light .year{color:#222}

  .syllables{position:absolute;top:30px;left:0;right:0;font-family:"Cormorant Garamond",Georgia,serif;font-weight:500;letter-spacing:2px}
  .syllables span{display:block}
  .syllables--red{color:var(--red);font-size:40px;line-height:42px}
  .syllables--gold{color:var(--gold);font-size:33px;line-height:34px}
  .syllables--rose{color:var(--rose);font-size:40px;line-height:44px}

  .landscape{position:absolute;left:0;right:0;top:158px;height:44px}
  .label--dark .landscape{background:linear-gradient(180deg,rgba(30,30,30,0),#1c1c1c 60%,rgba(20,20,20,0.3))}
  .label--light .landscape{background:linear-gradient(180deg,rgba(225,225,225,0),#e4e4e4 55%,rgba(240,240,240,0.3))}

  .brand{position:absolute;left:0;right:0;display:flex;justify-content:center;align-items:center;gap:5px}
  .brand-mark{width:9px;height:9px;border-radius:50%}
  .brand-name{font-family:"Lato",Arial,sans-serif;font-weight:400;font-size:8px;letter-spacing:1px;line-height:1}
  .label--dark .brand-name{color:#eeeeee}
  .label--light .brand-name{color:#1a1a1a}

  .made-in{position:absolute;left:0;right:0;font-size:5.5px;letter-spacing:1.1px}
  .label--dark .made-in{color:#ddd}
  .label--light .made-in{color:#333}

  .temp-name{position:absolute;left:0;right:0;top:120px;font-family:"Cormorant Garamond",Georgia,serif;font-weight:500;font-size:12px;line-height:15px;color:var(--ink)}

  .back-brand{top:14px}
  .region{position:absolute;top:33px;left:0;right:0;font-size:6px;font-weight:300}
  .wine-name{position:absolute;top:43px;left:0;right:0;font-family:"Cormorant Garamond",Georgia,serif;font-weight:500;font-size:24px;line-height:26px}
  .variety{position:absolute;top:70px;left:0;right:0;font-size:8px;font-weight:300;letter-spacing:0.5px}
  .label--dark .variety{color:#aaa}
  .label--light .variety{color:#222}
  .dryness{position:absolute;top:81px;left:0;right:0;font-size:5.5px;font-weight:300;line-height:7px}
  .story{position:absolute;top:104px;left:8px;right:8px;font-size:5.2px;font-weight:300;line-height:7px}
  .legal{position:absolute;top:132px;left:6px;right:6px;font-size:5.2px;font-weight:300;line-height:7px}
  .footer{position:absolute;bottom:6px;left:10px;right:10px;display:flex;justify-content:space-between;font-size:6.5px;font-weight:300}
  .footer--red{color:var(--red)}
  .footer--gold{color:var(--gold)}
  .footer--rose{color:var(--rose)}
</style>
</head>
<body>

<!-- Pelmik front -->
<section class="label label--front label--dark" style="left:65px">
  <div class="year">2017</div>
  <div class="syllables syllables--red"><span>PE</span><span>LM</span><span>IK</span></div>
  <div class="landscape" role="img" aria-label="Faint etched vineyard landscape"></div>
  <div class="brand" style="top:210px">
    <span class="brand-mark" style="background:var(--red)"></span>
    <span class="brand-name">KLET DOLINAR</span>
  </div>
  <div class="made-in" style="top:233px">IZDELANO V SLOVENIJI</div>
</section>

<!-- Pelmik back -->
<section class="label label--back label--dark" style="left:240px">
  <div class="brand back-brand">
    <span class="brand-mark" style="background:var(--red)"></span>
    <span class="brand-name">KLET DOLINAR</span>
  </div>
  <div class="region">VINORODNI OKOLIŠ KRAS</div>
  <div class="wine-name" style="color:var(--red)">PELMIK</div>
  <div class="variety">TERAN PTP</div>
  <div class="dryness">suho vino<br>2017</div>
  <p class="story">Izdelan po tradicionalnem postopku iz izbranega grozdja teranovk z Dolinarjevih starih brajd na Pelmiku.</p>
  <p class="legal">Vsebuje sulfit.<br>Št. polnitve: 10-2018. Št. odločbe: LJ-540/2018.<br>IZDELANO V SLOVENIJI - MADE IN SLOVENIA</p>
  <div class="footer footer--red"><span>11,0 % vol</span><span>0,75 l</span></div>
</section>

<!-- Ostrena front -->
<section class="label label--front label--light" style="left:440px">
  <div class="year">2017</div>
  <div class="syllables syllables--gold"><span>OS</span><span>TR</span><span>EN</span><span>A</span></div>
  <div class="landscape" role="img" aria-label="Faint etched vineyard landscape" style="top:166px;height:38px"></div>
  <div class="brand" style="top:210px">
    <span class="brand-mark" style="background:var(--gold)"></span>
    <span class="brand-name">KLET DOLINAR</span>
  </div>
  <div class="made-in" style="top:233px">IZDELANO V SLOVENIJI</div>
</section>

<!-- Ostrena back -->
<section class="label label--back label--light" style="left:621px">
  <div class="brand back-brand">
    <span class="brand-mark" style="background:var(--gold)"></span>
    <span class="brand-name">KLET DOLINAR</span>
  </div>
  <div class="region">VINORODNI OKOLIŠ KRAS</div>
  <div class="wine-name" style="color:var(--gold)">OSTRENA</div>
  <div class="variety">CHARDONNAY</div>
  <div class="dryness">suho vino<br>2017</div>
  <p class="story">Izdelan po tradicionalnem postopku iz izbranega grozdja s Dolinarjevih starih brajd na Ostreni.</p>
  <p class="legal">Vsebuje sulfit.<br>Št. polnitve: 10-2018. Št. odločbe: LJ-540/2018.<br>IZDELANO V SLOVENIJI - MADE IN SLOVENIA</p>
  <div class="footer footer--gold"><span>11,0 % vol</span><span>0,75 l</span></div>
</section>

<!-- Rosé front -->
<section class="label label--front label--light" style="left:825px;width:138px;height:236px">
  <div class="year">2017</div>
  <div class="syllables syllables--rose"><span>RO</span><span>SÉ</span></div>
  <div class="temp-name">temporary name rose<br>privremeno ime rose</div>
  <div class="landscape" role="img" aria-label="Faint etched vineyard landscape" style="top:156px;height:36px"></div>
  <div class="brand" style="top:199px">
    <span class="brand-mark" style="background:var(--rose)"></span>
    <span class="brand-name">KLET DOLINAR</span>
  </div>
  <div class="made-in" style="top:222px">IZDELANO V SLOVENIJI</div>
</section>

<!-- Rosé back -->
<section class="label label--back label--light" style="left:999px;top:324px;width:138px;height:185px">
  <div class="brand back-brand">
    <span class="brand-mark" style="background:var(--rose)"></span>
    <span class="brand-name">KLET DOLINAR</span>
  </div>
  <div class="region">VINORODNI OKOLIŠ KRAS</div>
  <div class="wine-name" style="color:var(--rose)">LOREM</div>
  <div class="variety">ROSÉ</div>
  <div class="dryness">suho vino<br>2017</div>
  <p class="story">Izdelan po tradicionalnem postopku iz izbranega grozdja teranovk z Dolinarjevih starih brajd na Pelmiku.</p>
  <p class="legal">Vsebuje sulfit.<br>Št. polnitve: 10-2018. Št. odločbe: LJ-540/2018.<br>IZDELANO V SLOVENIJI - MADE IN SLOVENIA</p>
  <div class="footer footer--rose"><span>11,0 % vol</span><span>0,75 l</span></div>
</section>

</body>
</html>
```